A3 Menus for new international restaurant in Singapore.

Looking for new A3 menu design for indoor & outdoor (beautiful garden and trees) restaurant that caters for expat and local families. International menu, cool jazz vibe, great for couples and families. Restaurant called Fern Quay Commons. I have attached some of the logos we use. Will consider black and white or color options. Restaurant located on a hill where there were tin mines many years ago, hence the name and branding. Looking for three menus (1) Dinner (2) Lunch (3) weekend brunch.

Target Market(s)

Families, young couples and professionals.

Industry/Entity Type

Restaurant

Font styles to use
Serif
Sans Serif

Requirements
Must have
• All food layout on one side of A3, one for each attached menu. Also a space for drinks list on the back.
Nice to have
• Use some of the logo material we have attached.
Should not have

```html
<!DOCTYPE html>
<html lang="en">
<head>
<meta charset="utf-8">
<title>Fern Quay Commons – Libations &amp; Dinner Menu</title>
<link href="https://fonts.googleapis.com/css2?family=Rye&family=Old+Standard+TT:wght@400;700&family=Special+Elite&display=swap" rel="stylesheet">
<style>
  :root{
    --backdrop:#2b241f;
    --rust-light:#b8743f;
    --rust:#9a5a2c;
    --rust-dark:#6e3a1a;
    --band:#5a2f14;
    --cream:#f2e3cf;
    --paper:#fbfaf7;
    --ink:#2a1d14;
    --heading:#a4561f;
    --disc:rgba(240,220,205,.38);
  }
  *{box-sizing:border-box;margin:0;padding:0}
  html,body{width:1200px;height:1000px;overflow:hidden;background:var(--backdrop)}
  .canvas{position:relative;width:1200px;height:1000px}
  .sheet{position:absolute;overflow:hidden;
    background:radial-gradient(ellipse at 40% 30%,var(--rust-light),var(--rust) 55%,var(--rust-dark));
    box-shadow:0 6px 18px rgba(0,0,0,.55)}
  .disc{position:absolute;border-radius:50%;background:var(--disc)}
  .paper{position:absolute;background:var(--paper)}
  .wordmark{position:absolute;font-family:"Rye",serif;color:var(--cream);text-align:center;white-space:nowrap}

  /* back: libations */
  .libations{left:83px;top:210px;width:527px;height:740px}
  .libations .wordmark{left:0;width:100%;top:48px;font-size:34px;line-height:1.5}
  .libations-title{position:absolute;top:272px;width:100%;text-align:center;font-family:"Old Standard TT",serif;font-weight:700;font-size:20px;letter-spacing:7px;color:var(--cream)}

  /* front: dinner */
  .dinner{left:652px;top:57px;width:528px;height:741px;font-family:"Old Standard TT",serif;color:var(--ink)}
  .band{position:absolute;left:0;top:0;width:100%;height:24px;background:var(--band);color:var(--cream);font-family:"Old Standard TT",serif;font-weight:700;font-size:19px;letter-spacing:9px;text-align:right;padding-right:48px;line-height:24px;word-spacing:22px}
  .dinner .wordmark{left:30px;top:34px;width:150px;font-size:21px;line-height:1.75}
  .section-title{font-family:"Rye",serif;font-size:19px;text-align:center;line-height:1.1}
  .on-rust .section-title{color:var(--cream)}
  .on-paper .section-title{color:var(--heading)}
  .item{text-align:center;margin-bottom:5px}
  .item-name{font-family:"Special Elite",serif;font-size:6.6px;text-transform:uppercase;display:block;line-height:1.25}
  .item-desc{font-size:5.6px;line-height:1.3;display:block}
  .on-rust .item{color:var(--cream)}
  .col{position:absolute}
  .list-line{font-size:6px;line-height:1.45}
  .list-line b{font-family:"Special Elite",serif;font-weight:400;text-transform:uppercase}
  .note{position:absolute;font-size:6px}
</style>
</head>
<body>
<div class="canvas">

  <section class="sheet libations" aria-label="Libations menu, back side">
    <div class="disc" style="left:-10px;top:-40px;width:135px;height:120px" role="img" aria-label="Faint illustration of a kettle"></div>
    <div class="disc" style="left:370px;top:30px;width:135px;height:135px" role="img" aria-label="Faint illustration of a fork"></div>
    <div class="disc" style="left:25px;top:330px;width:165px;height:165px" role="img" aria-label="Faint illustration of a teapot"></div>
    <div class="disc" style="left:417px;top:445px;width:130px;height:135px" role="img" aria-label="Faint illustration of a tankard"></div>
    <div class="wordmark">FERN<br>QUAY<br>COMMONS</div>
    <div class="libations-title">LIBATIONS</div>
    <div class="paper" style="left:122px;top:300px;width:285px;height:440px"></div>
  </section>

  <section class="sheet dinner" aria-label="Dinner menu">
    <div class="band">DINNER MENU</div>
    <div class="disc" style="left:10px;top:160px;width:110px;height:120px" role="img" aria-label="Faint illustration of a kettle"></div>
    <div class="disc" style="left:25px;top:605px;width:125px;height:130px" role="img" aria-label="Faint illustration of a fork"></div>
    <div class="wordmark">FERN<br>QUAY<br>COMMONS</div>

    <div class="col on-rust" style="left:50px;top:178px;width:145px">
      <h2 class="section-title" style="margin-bottom:14px">STARTERS</h2>
      <div class="item"><span class="item-name">Roasted Red Capsicum Soup</span><span class="item-desc">with popped rice and coconut cream $9.50</span></div>
      <div class="item"><span class="item-name">Classic Green Salad</span><span class="item-desc">cherry tomatoes, feta, kalamata olives, green capsicum &amp; cucumber $16.50</span></div>
      <div class="item"><span class="item-name">Beetroot Salad</span><span class="item-desc">slow-cooked beetroot, assorted onions, creamy goat's cheese, walnuts $17</span></div>
      <div class="item"><span class="item-name">Beef Tartare</span><span class="item-desc">hand-chopped sirloin and tenderloin mixed with capers, pickles &amp; shallots, served with bone marrow and crostini $22</span></div>
      <div class="item"><span class="item-name">Crab Salad</span><span class="item-desc">blue swimmer crab remoulade, tiger prawns, frisee salad leaves and homemade brioche melba toast $17.50</span></div>
      <div class="item"><span class="item-name">Duck Croquettes</span><span class="item-desc">crispy panko-coated duck rillettes, accompanied by parsnip mash, garlic confit and sweet wine sauce $16.50</span></div>
    </div>

    <div class="col on-rust" style="left:50px;top:478px;width:145px">
      <h2 class="section-title" style="margin-bottom:10px">DESSERTS</h2>
      <div class="item"><span class="item-name">Frozen Mojito</span><span class="item-desc">lime and rum sorbet with spearmint granita, soda foam and sugar crumbs $14</span></div>
      <div class="item"><span class="item-name">Gianduja Chocolate Fondant</span><span class="item-desc">with orange coulis and lime cremoso $15</span></div>
      <div class="item"><span class="item-name">Mango Chilli Pie</span><span class="item-desc">with rice pudding ice cream and coconut sago $15</span></div>
      <div class="item"><span class="item-name">Chocolate Cake</span><span class="item-desc">with raspberry coulis, vanilla ice cream and almond brittle $15</span></div>
      <div class="item"><span class="item-name">Hay-Infused Panna Cotta</span><span class="item-desc">with spiced honey sauce and apple butter $10</span></div>
      <div class="item"><span class="item-name">Ice Cream</span><span class="item-desc">your selection, per scoop $5</span></div>
      <div class="item"><span class="item-name">Cheese Board</span><span class="item-desc">selection of three worldwide cheeses, grapes, crostini and chutney $23</span></div>
    </div>

    <div class="paper on-paper" style="left:200px;top:24px;width:318px;height:702px">
      <div class="disc" style="left:205px;top:310px;width:95px;height:100px;background:rgba(160,110,80,.18)" role="img" aria-label="Faint illustration of a fork"></div>

      <div class="col" style="left:30px;top:6px;width:258px">
        <h2 class="section-title" style="margin-bottom:4px">PLATTERS</h2>
        <div class="item"><span class="item-name">Seafood Platter</span><span class="item-desc">selection of gravlax, smoked fish, marinated seafood,<br>pumpernickel bread and dipping sauces<br>$38 for 2 to share : $70 for 4 to share</span></div>
        <div class="item"><span class="item-name">Charcuterie Platter ⚲</span><span class="item-desc">3 types of charcuterie, duck rillettes, pickles, crostini and<br>wholegrain mustard<br>$32 for 2 to share : $60 for 4 to share</span></div>
      </div>

      <h2 class="section-title col" style="left:0;top:130px;width:100%">MAIN COURSES</h2>
      <div class="col" style="left:10px;top:156px;width:150px">
        <div class="item"><span class="item-name">Fern Quay Commons Burger</span><span class="item-desc">200gms ground prime beef served in a home-made brioche bun with lettuce, tomato and mayo served with a side of fries $22, top it with cheese or bacon or both – add $2 for each</span></div>
        <div class="item"><span class="item-name">Fern Quay Bangers &amp; Mash</span><span class="item-desc">prime pork sausages, buttery mashed potato covered in onion &amp; cider gravy $22</span></div>
        <div class="item"><span class="item-name">Hay Smoked Pork Ribs</span><span class="item-desc">home-smoked, slow-cooked ribs, served with spicy chimichurri sauce and fries $26</span></div>
        <div class="item"><span class="item-name">Pan Seared Black Cod</span><span class="item-desc">served on a bed of vermicelli, lemongrass, fresh chilli and kaffir lime leaves $35</span></div>
        <div class="item"><span class="item-name">Beef Tenderloin</span><span class="item-desc">200gms grilled to your choice, served with roasted vine tomatoes and red wine gravy, accompanied by buttery mashed potato or fries $35</span></div>
        <div class="item"><span class="item-name">Fern Quay's Seafood Stew</span><span class="item-desc">classic seafood stew, served in the pan with fresh black cod, prawns, calamari, clams and mussels, cooked in a prawn bisque, with bread for dipping $30</span></div>
      </div>
      <div class="col" style="left:168px;top:156px;width:140px">
        <div class="item"><span class="item-name">Roast Chicken ⚲</span><span class="item-desc">share a whole bird for 2, with jus and your choice of two sides. (Allow 25 mins to prepare) $38</span></div>
        <div class="item"><span class="item-name">Roast Pork Belly</span><span class="item-desc">served with apple compote and your choice of two sides. Whole belly shared among 3-4 people. (Allow 45 mins to roast.) $85</span></div>
        <div class="item"><span class="item-name">Beef T-Bone</span><span class="item-desc">600gms T-Bone grilled, served with red wine gravy and your choice of two sides (Shared among 2 people. Allow 25 mins to cook) $70</span></div>
        <div style="margin-top:8px">
          <p class="list-line"><b>Strigoli</b> – with beef ragu bolognese $22</p>
          <p class="list-line"><b>Linguini</b> – with a light creamy carbonara sauce, with smoked pancetta $23</p>
          <p class="list-line"><b>Rigatoni</b> – with aglio, olio and peperoncino $20, with prawns, add $5</p>
          <p class="list-line"><b>Risotto</b> – with rich porcini mushrooms and crutin cheese $22</p>
          <p class="list-line"><b>Margherita</b> – roast tomato, mozzarella and fresh basil $24</p>
        </div>
      </div>

      <h2 class="section-title col" style="left:0;top:426px;width:100%">PIZZAS</h2>
      <div class="col" style="left:10px;top:454px;width:300px">
        <p class="list-line"><b>Bloody Margherita</b> – a take on the classic aperitif: vodka flushed roast tomatoes, mozzarella, celery salt, worcester and tabasco sauces $28</p>
        <p class="list-line"><b>Spinach and Ricotta</b> – with toasted pine nuts, cherry tomatoes and ricotta cheese $25</p>
        <p class="list-line"><b>Umami Chicken</b> – with baby king oyster mushrooms, shaved parmesan and fresh thyme $27</p>
        <p class="list-line"><b>Parma Ham</b> – with semi-dried tomato and fresh arugula leaves $29</p>
        <p class="list-line"><b>Hay-Smoked Pulled Pork and Pancetta</b> – home-smoked, slow cooked pulled pork rib, with sausage, pancetta and onion $29</p>
        <p class="list-line"><b>Smoked Pancetta</b> – with shitake mushrooms, spring onions, chilli and brie $29</p>
        <p class="list-line"><b>⚲ Seafood</b> – with smoked salmon, prawns, calamari, onions, and crushed roasted tomato $30</p>
      </div>

      <h2 class="section-title col" style="left:0;top:574px;width:100%">SIDES</h2>
      <div class="col" style="left:10px;top:604px;width:300px;text-align:center">
        <p class="list-line"><b>Coconut Corn on the Cob / Onion Mashed Potato /</b></p>
        <p class="list-line"><b>Peas and Smoked Pancetta /</b></p>
        <p class="list-line"><b>Green Beans with Toasted Pine Nuts and Garlic Confit /</b></p>
        <p class="list-line"><b>Mixed Salad / Truffle Fries / French Fries</b> $7</p>
        <p class="list-line"><b>Bread Rolls</b> – with olive oil and balsamic vinegar $4</p>
      </div>
      <p class="note" style="left:8px;top:684px">⚲ Fern Quay Specialty</p>
    </div>

    <p class="note" style="left:210px;top:729px;color:var(--ink)">All prices are in Singapore Dollars and are subject to GST &amp; 10% Service Charge</p>
  </section>

</div>
</body>
</html>
```